Personal training poster - 1200X900mm

Poster to promote my new personal training service at my gym. The poster will be printed and put into an aframe to be seen by people walking past my gym. It needs to be simple and eye catching with the text i have put in the must haves. The text and image should be the prominent parts of the design.

Target Market(s)

30-50 year old females

Industry/Entity Type

Fitness

Font styles to use
Sans Serif

Requirements
Must have
• my logo
• exercise graphic
• Must include the following text:
• Are you looking for a personal trainer? Our expert trainers can help you achieve you take your health and fitness back!
• Contact details:
• 1300452968
• info@brightmovegym.com.au
• Located under the Harbourview Club

```html
<!DOCTYPE html>
<html lang="en">
<head>
<meta charset="utf-8">
<title>Personal Training Poster – Brightmove Gym</title>
<link href="https://fonts.googleapis.com/css2?family=Bebas+Neue&family=Roboto:wght@400&display=swap" rel="stylesheet">
<style>
  :root {
    --page: #ffffff;
    --navy: #132247;
    --navy-deep: #0f1c3d;
    --royal: #1f4fae;
    --royal-soft: #2a62c9;
    --sun: #fdc32f;
    --sun-light: #fde84a;
    --teal: #17b4d1;
    --sky: #2aa6e6;
    --white: #ffffff;
  }
  * { margin: 0; padding: 0; box-sizing: border-box; }
  html, body {
    width: 990px; height: 1200px; overflow: hidden;
    background: var(--page);
  }
  .poster {
    position: absolute; left: 61px; top: 22px;
    width: 866px; height: 1155px;
    background: var(--navy);
    overflow: hidden;
    font-family: "Roboto", Arial, sans-serif;
    color: var(--white);
  }
  .backdrop { position: absolute; inset: 0; }
  .exercise-photo {
    position: absolute; left: 54px; top: 41px;
    width: 412px; height: 528px;
    background: linear-gradient(160deg, #c99a7a 0%, #3a2a25 28%, #111111 60%, #1a1a1a 100%);
    clip-path: polygon(45% 0, 70% 0, 88% 45%, 100% 78%, 100% 100%, 0 100%, 10% 60%, 30% 22%);
  }
  .brand {
    position: absolute; left: 465px; top: 300px; width: 351px;
    display: flex; align-items: center; justify-content: center; gap: 14px;
  }
  .brand-dot {
    width: 52px; height: 52px; border-radius: 50%;
    background: var(--sun);
  }
  .brand-name {
    font-family: "Bebas Neue", "Arial Narrow", sans-serif;
    font-size: 60px; line-height: 1; color: var(--sun);
    letter-spacing: 1px;
  }
  .headline {
    position: absolute; left: 58px; top: 616px;
    font-family: "Bebas Neue", "Arial Narrow", sans-serif;
    line-height: 1; letter-spacing: -1px;
  }
  .headline-lead { display: block; font-size: 84px; color: var(--teal); }
  .headline-key { display: block; font-size: 90px; color: var(--sun); margin-top: 4px; }
  .pitch {
    position: absolute; left: 61px; top: 801px; width: 640px;
    font-size: 24.5px; line-height: 44px;
  }
  .contacts { position: absolute; left: 61px; top: 922px; list-style: none; }
  .contact {
    display: flex; align-items: center; height: 46px; margin-bottom: 27px;
    font-size: 29px; letter-spacing: 0.3px;
  }
  .contact-icon { width: 46px; height: 46px; margin-right: 25px; flex: none; }
</style>
</head>
<body>
<main class="poster">
  <svg class="backdrop" width="866" height="1155" viewBox="0 0 866 1155" aria-hidden="true">
    <polygon points="0,0 713,0 0,500" fill="var(--sun)"/>
    <polygon points="168,36 258,250 70,500 0,500 0,470" fill="var(--sun-light)"/>
    <polygon points="100,330 300,300 26,624" fill="var(--royal)" opacity="0.7"/>
    <polygon points="678,620 866,720 866,900 760,1140" fill="var(--royal)" opacity="0.75"/>
    <polygon points="750,800 866,870 866,1000 805,1130" fill="var(--royal-soft)" opacity="0.8"/>
  </svg>

  <div class="exercise-photo" role="img" aria-label="Woman in black activewear seated in a yoga twist, seen from behind"></div>

  <div class="brand">
    <span class="brand-dot"></span>
    <span class="brand-name">Brightmove Gym</span>
  </div>

  <h1 class="headline">
    <span class="headline-lead">Are you looking for a</span>
    <span class="headline-key">Personal Trainer?</span>
  </h1>

  <p class="pitch">Our expert trainers can help you take your health and fitness back!</p>

  <ul class="contacts">
    <li class="contact">
      <svg class="contact-icon" viewBox="0 0 46 46" aria-hidden="true">
        <path d="M9 4c3 0 6 6 7 9 1 2-3 4-3 6 1 5 7 11 12 13 2 0 4-4 6-3 3 1 9 4 9 7 0 4-5 7-9 7C18 42 4 28 3 12 3 8 6 4 9 4z" fill="var(--sky)"/>
        <path d="M28 10a8 8 0 0 1 8 8M28 4a14 14 0 0 1 14 14" stroke="var(--sun)" stroke-width="3" fill="none" stroke-linecap="round"/>
      </svg>
      <span>1300452968</span>
    </li>
    <li class="contact">
      <svg class="contact-icon" viewBox="0 0 46 46" aria-hidden="true">
        <rect x="1" y="8" width="44" height="30" fill="var(--sky)"/>
        <path d="M1 8l22 17L45 8" stroke="var(--sun)" stroke-width="3" fill="none"/>
        <path d="M1 38l16-14M45 38L29 24" stroke="var(--navy)" stroke-width="2" fill="none"/>
      </svg>
      <span>info@brightmovegym.com.au</span>
    </li>
    <li class="contact">
      <svg class="contact-icon" viewBox="0 0 46 46" aria-hidden="true">
        <path d="M23 2c9 0 16 7 16 16 0 11-16 26-16 26S7 29 7 18C7 9 14 2 23 2z" fill="var(--sky)"/>
        <circle cx="23" cy="18" r="6" fill="var(--sun)"/>
      </svg>
      <span>Located under the Harbourview Club</span>
    </li>
  </ul>
</main>
</body>
</html>
```